Lumora App | Pre-Launch Homepage

Dear designer,
Lumora is a soon to be launched innovative & free social platform for collaborative addictions quitting.
We require a design for our pre-launch homepage that will elevate our basic wireframes to the next level.
We would like the wireframes to serve as a guideline only, and not as a final version of the design. If you have cool ideas - we would appreciate your creativity!
* This is a pre-launch website for a mobile app, and as such the design must be consistent with the general style, design and atmosphere of the app (see screenshot in the shared Drive link).
* We liked the style and feel of the following website: http://palvexapp.com/ - Please let's use it as a reference as well.
* The existing text in the wireframes is there just to represent a place for text. Copy will be edited by us after the design is done.
Please find the wireframes attached, and all relevant design assets and app screenshots in the following Drive shared link -
https://files.norvakshare.com/open?id=7Q284KtP3mXcRf8Hj21W5vLzDne
Thanks,
Marcus
Industry/Entity Type
Social
Number of Pages Required
1 page
Look and feel
Each slider illustrates characteristics of the customer's brand and the style your logo design should communicate.

```html
<!DOCTYPE html>
<html lang="en">
<head>
<meta charset="utf-8">
<title>Lumora App | Pre-Launch Homepage</title>
<link href="https://fonts.googleapis.com/css2?family=Open+Sans:wght@400;600;700;800&display=swap" rel="stylesheet">
<style>
:root{
  --hero-bg:#3a2f22;
  --hero-bg-2:#2c241a;
  --orange:#f7941d;
  --orange-deep:#ef7d0f;
  --red:#e02127;
  --green:#2aa43c;
  --green-btn:#3ea32a;
  --blue:#29a8e0;
  --sky:#8dd7f5;
  --grey-band:#e6e6e6;
  --text:#333333;
  --muted:#666666;
  --white:#ffffff;
  --olive:#4a4331;
  --footer:#2b2720;
  --device:#1c1c1c;
}
*{box-sizing:border-box;margin:0;padding:0}
html,body{width:1200px;height:3712px;overflow:hidden}
body{font-family:"Open Sans",Arial,sans-serif;color:var(--text);background:var(--white)}
section{position:relative;width:1200px;overflow:hidden}

/* hero */
.hero{height:632px;background:linear-gradient(180deg,var(--hero-bg),var(--hero-bg-2))}
.brand{position:absolute;left:176px;top:40px;font-size:72px;font-weight:800;color:var(--orange);line-height:1}
.tagline{position:absolute;left:176px;top:124px;font-size:22px;color:var(--orange);font-weight:600}
.hero-lead{position:absolute;left:176px;top:232px;width:520px;font-size:30px;line-height:40px;color:var(--white);font-weight:700}
.subscribe-label{position:absolute;font-size:16px;font-weight:600;color:var(--orange)}
.hero .subscribe-label{left:176px;top:408px}
.subscribe{position:absolute;display:flex;gap:8px}
.hero .subscribe{left:176px;top:438px}
.subscribe .field{width:260px;height:44px;background:var(--white);border:1px solid #ccc}
.subscribe .btn{height:44px;padding:0 18px;background:var(--green-btn);color:var(--white);font-size:15px;font-weight:600;display:flex;align-items:center}
.contact-btn{position:absolute;right:220px;top:40px;background:var(--orange);color:var(--white);font-size:15px;font-weight:600;padding:8px 18px}
.phone{position:absolute;left:786px;top:108px;width:216px;height:440px;background:#f2f2f2;border-radius:36px;border:3px solid #d0d0d0;padding:60px 12px}
.phone .screen{width:100%;height:100%;background:linear-gradient(180deg,#4b3a2a,#f3e6d6 35%,#ffffff)}

/* features */
.features{height:548px;background:var(--white)}
.feature{position:absolute;top:112px;width:240px;text-align:center}
.feature svg{display:block;margin:0 auto}
.feature h3{margin-top:40px;font-size:22px;font-weight:600;color:var(--text)}
.feature p{margin:10px auto 0;width:200px;font-size:13px;line-height:18px;color:var(--muted)}

/* fun */
.fun{height:408px;background:var(--grey-band)}
.fun .photo{position:absolute;left:0;top:0;width:600px;height:408px;background:linear-gradient(90deg,#d9d6d0,#bfae98 55%,#e2e0dc)}
.copy{position:absolute;width:440px}
.copy h2{font-size:30px;font-weight:400;letter-spacing:1px}
.copy p{margin-top:14px;font-size:14px;line-height:21px}
.fun .copy{left:660px;top:92px}
.fun h2{color:var(--blue)}
.hl{color:var(--blue)}

/* inspire */
.inspire{height:432px;background:linear-gradient(180deg,var(--orange),var(--orange-deep))}
.inspire .ring{position:absolute;left:60px;top:20px;width:340px;height:340px;border-radius:50%;border:2px solid rgba(255,255,255,.25)}
.inspire .copy{left:200px;top:120px;width:400px;color:var(--white)}
.inspire h2{color:var(--white)}
.tablet{position:absolute;background:var(--device);border-radius:26px;padding:34px}
.tablet .screen{width:100%;height:100%}
.inspire .tablet{left:620px;top:28px;width:520px;height:380px;transform:rotate(-4deg)}
.crowd{background:linear-gradient(160deg,#c8d6e4,#e6b48c 50%,#8e6c50)}

/* achieve */
.achieve{height:620px;background:var(--sky)}
.achieve h2{position:absolute;left:0;right:0;top:28px;text-align:center;font-size:32px;font-weight:400;color:var(--text);letter-spacing:1px}
.achieve .intro{position:absolute;left:400px;width:400px;top:84px;text-align:center;font-size:13px;line-height:18px}
.achieve .accent{position:absolute;left:0;right:0;top:140px;text-align:center;font-size:13px;color:var(--orange-deep)}
.achieve .photo{position:absolute;left:440px;top:180px;width:320px;height:440px;background:linear-gradient(180deg,var(--sky),#c98d6e 40%,#5a6a8a)}
.point{position:absolute;width:200px;text-align:center;font-size:12px;line-height:16px}
.point svg{display:block;margin:0 auto 10px}

/* coming soon */
.soon{height:688px;background:var(--white)}
.soon h2{position:absolute;left:0;right:0;top:44px;text-align:center;font-size:34px;font-weight:700;color:var(--orange)}
.soon .tablet{left:380px;top:128px;width:440px;height:340px}
.arrow{position:absolute;top:278px;width:56px;height:56px;border-radius:50%;background:#e4e4e4}
.stores{position:absolute;top:532px;left:0;right:0;display:flex;justify-content:center;gap:100px}
.store{width:100px;height:100px;border-radius:22px;background:#d8d8d8}

/* join */
.join{height:336px;background:var(--olive);text-align:center}
.join h2{position:absolute;left:0;right:0;top:32px;font-size:50px;font-weight:400;color:var(--white);letter-spacing:2px}
.join .subscribe-label{left:0;right:0;top:116px}
.join .subscribe{left:412px;top:148px}
.socials{position:absolute;left:0;right:0;top:222px;display:flex;justify-content:center;gap:14px}
.socials span{width:38px;height:38px;border-radius:50%;background:var(--blue)}
.links{position:absolute;left:0;right:0;top:284px;font-size:15px;color:var(--white)}

.site-footer{height:48px;background:var(--footer);color:#aaa;font-size:12px;display:flex;align-items:center;justify-content:center}
</style>
</head>
<body>

<section class="hero">
  <div class="brand">Lumora</div>
  <div class="tagline">Become a Better Version of Yourself</div>
  <a class="contact-btn">Contact Us</a>
  <p class="hero-lead">Lumora is a revolutionary &amp; free social platform for collaborative addictions quitting</p>
  <p class="subscribe-label">Subscribe Below for Beta Release and Updates</p>
  <div class="subscribe"><span class="field"></span><span class="btn">Let Me Know</span></div>
  <div class="phone"><div class="screen" role="img" aria-label="App screenshot showing a user profile screen"></div></div>
</section>

<section class="features">
  <div class="feature" style="left:150px">
    <svg width="200" height="220" viewBox="0 0 200 220"><polygon points="100,0 195,55 195,165 100,220 5,165 5,55" fill="var(--orange)"/><polygon points="100,60 112,94 148,94 119,115 130,150 100,129 70,150 81,115 52,94 88,94" fill="#fff"/></svg>
    <h3>Never be Alone</h3>
    <p>Forget what you know - Lumora makes it fun to quit</p>
  </div>
  <div class="feature" style="left:480px">
    <svg width="200" height="220" viewBox="0 0 200 220"><polygon points="100,0 195,55 195,165 100,220 5,165 5,55" fill="var(--red)"/><circle cx="100" cy="110" r="46" fill="none" stroke="#fff" stroke-width="20"/></svg>
    <h3>Network Power</h3>
    <p>Forget what you know - Lumora makes it fun to quit</p>
  </div>
  <div class="feature" style="left:810px">
    <svg width="200" height="220" viewBox="0 0 200 220"><polygon points="100,0 195,55 195,165 100,220 5,165 5,55" fill="var(--green)"/><polyline points="60,112 90,142 145,82" fill="none" stroke="#fff" stroke-width="20" stroke-linecap="round" stroke-linejoin="round"/></svg>
    <h3>Stay Motivated</h3>
    <p>Forget what you know - Lumora makes it fun to quit</p>
  </div>
</section>

<section class="fun">
  <div class="photo" role="img" aria-label="Smiling man using a tablet on a sofa"></div>
  <div class="copy">
    <h2>FUN</h2>
    <p>Forget what you know - <span class="hl">Lumora makes it fun to quit</span>. The hurdle between your quest and real decisions comes to life in <span class="hl">our gamified approach</span> for reshaping your days.</p>
    <p><span class="hl">Lumora</span> gives you the opportunity to take an active role in helping your network to quit and reach your goals as a team. That's right, we converted the quitting journey into a social game.</p>
  </div>
</section>

<section class="inspire">
  <div class="ring"></div>
  <div class="copy">
    <h2>INSPIRE</h2>
    <p>One of the most important factors for successful quitting is the ability to stay inspired during the journey.</p>
    <p>Those who are stronger today on a platform around you can inspire and be inspired by a true journey of personal growth.</p>
  </div>
  <div class="tablet"><div class="screen crowd" role="img" aria-label="Group of cheering friends on a tablet screen"></div></div>
</section>

<section class="achieve">
  <h2>ACHIEVE</h2>
  <p class="intro">Lumora is built on a pyramid of relationships that makes use of the Social Cognitive Theory, to provide a powerful network of positive reinforcement.</p>
  <p class="accent">The biggest key factor in the success of your journey</p>
  <div class="photo" role="img" aria-label="Happy couple, man giving a piggyback ride"></div>
  <div class="point" style="left:190px;top:260px"><svg width="56" height="62" viewBox="0 0 56 62"><polygon points="28,0 56,16 56,46 28,62 0,46 0,16" fill="var(--orange)"/></svg>Lumora is built on a pyramid of relationships that makes use of the Social Cognitive Theory</div>
  <div class="point" style="left:810px;top:260px"><svg width="56" height="62" viewBox="0 0 56 62"><polygon points="28,0 56,16 56,46 28,62 0,46 0,16" fill="var(--green)"/></svg>Lumora is built on a pyramid of relationships that makes use of the Social Cognitive Theory</div>
  <div class="point" style="left:190px;top:404px"><svg width="56" height="62" viewBox="0 0 56 62"><polygon points="28,0 56,16 56,46 28,62 0,46 0,16" fill="var(--blue)"/></svg>Lumora is built on a pyramid of relationships that makes use of the Social Cognitive Theory</div>
  <div class="point" style="left:810px;top:404px"><svg width="56" height="62" viewBox="0 0 56 62"><polygon points="28,0 56,16 56,46 28,62 0,46 0,16" fill="#d0d0d0"/></svg>Lumora is built on a pyramid of relationships that makes use of the Social Cognitive Theory</div>
</section>

<section class="soon">
  <h2>COMING SOON</h2>
  <span class="arrow" style="left:186px"><svg width="56" height="56" viewBox="0 0 56 56"><polyline points="32,18 22,28 32,38" fill="none" stroke="#fff" stroke-width="5"/></svg></span>
  <div class="tablet"><div class="screen crowd" role="img" aria-label="Group of cheering friends on a tablet screen"></div></div>
  <span class="arrow" style="right:186px"><svg width="56" height="56" viewBox="0 0 56 56"><polyline points="24,18 34,28 24,38" fill="none" stroke="#fff" stroke-width="5"/></svg></span>
  <div class="stores"><span class="store"></span><span class="store"></span><span class="store"></span></div>
</section>

<section class="join">
  <h2>JOIN THE REVOLUTION</h2>
  <p class="subscribe-label">Subscribe Below for Beta Release and Updates</p>
  <div class="subscribe"><span class="field"></span><span class="btn">Let Me Know</span></div>
  <div class="socials"><span></span><span></span><span></span></div>
  <p class="links">Contact Us / T&amp;C's / Privacy Policy</p>
</section>

<footer class="site-footer">Copyright © 2015 Lumora Ltd.</footer>

</body>
</html>
```